tri-fold brochure design for psychology practice - all content provided

we are a psychology practice that specialises in diagnostic and educational assessments for children, adolescents and adults. We have an existing logo and I am attaching a word doc (tri-fold brochure) with the required content. I am also attaching our logo and other relevant content docs. The layout is only a sample and we are looking for someone to put this together into a consistent and better layout.

Target Market(s)

parents

Industry/Entity Type

education and health

Font styles to use
Other font styles liked:
• crimsonpro

Requirements
Must have
• our logo and the provided content

```html
<!DOCTYPE html>
<html lang="en">
<head>
<meta charset="utf-8">
<title>thebrightpath – tri-fold brochure</title>
<link rel="stylesheet" href="https://fonts.googleapis.com/css2?family=Hind:wght@400;500;600;700&family=Bebas+Neue&display=swap">
<style>
:root{
  --bg:#dcdcdc;
  --paper:#ffffff;
  --ink:#2f2f2f;
  --green:#6fb043;
  --green-dark:#5a9833;
  --green-light:#8cc63f;
  --blue:#5d9fd6;
  --teal:#52c28f;
  --leaf:#6aad45;
  --step:#dde9df;
  --grey-curve:#8a8a8a;
  --pill:#333333;
}
*{box-sizing:border-box;margin:0;padding:0}
html,body{width:1200px;height:1200px;overflow:hidden}
body{background:var(--bg);font-family:"Hind",sans-serif;color:var(--ink);position:relative}
.sheet{position:absolute;left:244px;width:716px;height:505px;background:var(--paper);display:flex;box-shadow:0 6px 18px rgba(0,0,0,.25)}
.sheet--outside{top:71px}
.sheet--inside{top:632px}
.panel{position:relative;width:238.67px;height:100%;overflow:hidden}
.panel + .panel{box-shadow:inset 8px 0 10px -8px rgba(0,0,0,.12)}

/* wave bands */
.wave{position:absolute;left:0;bottom:0;width:100%;display:block}
.web-line{position:absolute;left:0;width:100%;text-align:center;color:#fff;font-size:9.5px;letter-spacing:1.3px;font-weight:500}

/* stage boxes */
.stage{position:absolute;left:24px;width:190px;border-radius:6px;color:#fff;padding:0 12px;text-align:center}
.stage h3{font-size:9.8px;font-weight:700;letter-spacing:.2px;margin-bottom:1px}
.stage p{font-size:9.4px;line-height:11.2px;text-align:justify}
.stage svg{display:block;margin:0 auto}
.stage--understanding{top:22px;height:110px;background:var(--blue);padding-top:4px}
.stage--identifying{top:165px;height:117px;background:var(--teal);padding-top:4px}
.stage--guiding{top:312px;height:113px;background:var(--leaf);padding-top:4px}
.down-arrow{position:absolute;left:107px;display:block}

/* brand */
.brand{position:absolute;left:0;width:100%;display:flex;flex-direction:column;align-items:center}
.brand-dot{width:22px;height:22px;border-radius:50%;background:var(--green);margin-bottom:6px}
.brand-name{font-family:"Hind",sans-serif;font-weight:600;color:var(--ink);line-height:1}
.brand--light .brand-dot{background:#fff}
.brand--light .brand-name{color:#fff}

/* contact */
.map{position:absolute;left:22px;top:23px;width:195px;height:124px;border:3px solid var(--green-light);border-radius:8px;background:linear-gradient(135deg,#f1f1ef,#e4e6e2 60%,#eceee9);box-shadow:0 5px 8px rgba(0,0,0,.18)}
.contact-btn{position:absolute;left:70px;top:321px;width:98px;height:20px;border-radius:10px;background:var(--green);color:#fff;font-weight:700;font-size:11px;text-align:center;line-height:22px;letter-spacing:.3px}
.contact-icon{position:absolute;left:112px;width:14px;height:14px}
.contact-text{position:absolute;left:0;width:100%;text-align:center;font-size:10.5px;line-height:12.5px;font-weight:500}

/* cover */
.cover-photo{position:absolute;left:0;top:140px;width:100%;height:250px;background:linear-gradient(120deg,#eef0f2 0%,#d9c7b8 35%,#f2f2f2 55%,#7c95c9 78%,#e9e5e0 100%)}
.cover-band{position:absolute;left:0;bottom:0;width:100%;height:140px}
.cover-title{position:absolute;left:0;width:100%;text-align:center;font-family:"Bebas Neue",sans-serif;color:#fff;font-size:29px;line-height:31px;letter-spacing:.3px}
.pill{position:absolute;left:35px;top:469px;width:169px;height:20px;border-radius:10px;background:var(--pill);color:#fff;font-size:9.3px;letter-spacing:1.2px;text-align:center;line-height:21px}

/* inside */
.section-title{position:absolute;left:24px;top:23px;font-weight:700;color:var(--green);font-size:15px;line-height:16px}
.body-copy{position:absolute;left:24px;width:190px;font-size:10px;line-height:12.4px;text-align:justify}
.body-copy p + p{margin-top:12px}
.body-copy--who{font-size:9.8px;line-height:11.8px}
.who-photo{position:absolute;left:0;top:180px;width:100%;height:225px;background:linear-gradient(to bottom,#fff 0%,rgba(255,255,255,0) 22%),linear-gradient(100deg,#f4f4f4 0%,#e6ddd3 40%,#f6f3ef 65%,#d8c4ae 100%)}
.includes-title{position:absolute;left:24px;top:242px;font-size:10.8px;font-weight:500}
.conditions{position:absolute;left:24px;top:262px;list-style:none;font-size:10px}
.conditions li{display:flex;align-items:center;height:20.4px}
.conditions svg{margin-right:4px;flex:none}

.step{position:absolute;left:25px;width:189px;background:var(--step);border-radius:7px;padding:8px 9px 0 9px;font-size:9px;line-height:11.2px;text-align:justify}
.step p{text-indent:22px}
.step-num{position:absolute;left:-1px;top:-9px;width:26px;height:26px;border-radius:50%;background:var(--green);border:2px solid #fff;box-shadow:0 0 0 1px var(--green);color:#fff;font-weight:700;font-size:16px;line-height:27px;text-align:center}
.step-arrow{position:absolute;left:107px;display:block}
</style>
</head>
<body>

<section class="sheet sheet--outside">

  <div class="panel panel--approach">
    <div class="stage stage--understanding">
      <svg width="30" height="32" viewBox="0 0 30 32" fill="none" stroke="#fff" stroke-width="1.3">
        <circle cx="15" cy="8" r="4.5"/><path d="M13 13h4M15 1v1.5M8 8H9.5M20.5 8H22M10 3l1 1M20 3l-1 1"/>
        <circle cx="5" cy="20" r="2.2"/><path d="M1 30v-4a4 4 0 0 1 8 0v4"/>
        <circle cx="25" cy="20" r="2.2"/><path d="M21 30v-4a4 4 0 0 1 8 0v4"/>
        <rect x="11" y="21" width="8" height="6" rx="1"/>
      </svg>
      <h3>UNDERSTANDING</h3>
      <p>Assessment starts with listening first, and then asking the right questions in order to ensure that we are understanding your concerns and hearing your questions.</p>
    </div>
    <svg class="down-arrow" style="top:138px" width="26" height="24" viewBox="0 0 26 24" fill="var(--blue)"><rect x="7" y="0" width="12" height="2"/><rect x="7" y="3.5" width="12" height="2"/><rect x="7" y="7" width="12" height="2"/><path d="M0 11h26L13 24z"/></svg>

    <div class="stage stage--identifying">
      <svg width="32" height="32" viewBox="0 0 32 32" fill="none" stroke="#fff" stroke-width="1.4">
        <circle cx="19" cy="12" r="9"/><circle cx="19" cy="12" r="6"/>
        <path d="M12.5 18.5 3 28l2 2 9.5-9.5"/><path d="M19 8v4M19 14.5v.5"/>
      </svg>
      <h3>IDENTIFYING</h3>
      <p>It is then our job to use our diagnostic and assessment knowledge and skills to collect the right data in order to address your concerns and provide answers to your questions.</p>
    </div>
    <svg class="down-arrow" style="top:285px" width="26" height="24" viewBox="0 0 26 24" fill="var(--teal)"><rect x="7" y="0" width="12" height="2"/><rect x="7" y="3.5" width="12" height="2"/><rect x="7" y="7" width="12" height="2"/><path d="M0 11h26L13 24z"/></svg>

    <div class="stage stage--guiding">
      <svg width="32" height="34" viewBox="0 0 32 34" fill="none" stroke="#fff" stroke-width="1.4">
        <circle cx="16" cy="9" r="7.5"/><circle cx="16" cy="7" r="2.3"/><path d="M11.5 14a4.5 4.5 0 0 1 9 0"/>
        <path d="M16 17v16M3 25h26M16 33l-2.5-3M16 33l2.5-3M3 25l3-2.5M3 25l3 2.5M29 25l-3-2.5M29 25l-3 2.5"/>
      </svg>
      <h3>GUIDING</h3>
      <p>This then enables us to provide you with recommendations for accessing support and interventions that are based on current best practice and are suported by evidence.</p>
    </div>

    <svg class="wave" width="239" height="82" viewBox="0 0 239 82" preserveAspectRatio="none">
      <path d="M0 0C70 30 160 36 239 26V31C160 42 70 38 0 7Z" fill="var(--grey-curve)"/>
      <path d="M0 12C70 40 160 44 239 34V82H0Z" fill="var(--green)"/>
    </svg>
    <div class="web-line" style="top:476px">www.thebrightpath.com.au</div>
  </div>

  <div class="panel panel--contact">
    <div class="map" role="img" aria-label="Street map showing the practice location"></div>

    <div class="brand" style="top:188px">
      <span class="brand-dot"></span>
      <span class="brand-name" style="font-size:27px">thebrightpath</span>
    </div>

    <div class="contact-btn">CONTACT US</div>

    <svg class="contact-icon" style="top:355px" viewBox="0 0 14 14"><circle cx="7" cy="7" r="7" fill="var(--green)"/><path d="M7 3.2a2.4 2.4 0 0 0-2.4 2.4C4.6 7.5 7 10.5 7 10.5s2.4-3 2.4-4.9A2.4 2.4 0 0 0 7 3.2z" fill="#fff"/><circle cx="7" cy="5.6" r=".9" fill="var(--green)"/></svg>
    <div class="contact-text" style="top:372px">12/48 Harbour View Rd, Seabrook<br>NSW 2199</div>

    <svg class="contact-icon" style="top:400px" viewBox="0 0 14 14"><circle cx="7" cy="7" r="7" fill="var(--green)"/><path d="M4.3 3.6l1.5-.3.8 2-1 .8a5 5 0 0 0 2.3 2.3l.8-1 2 .8-.3 1.5c-3.3.2-6.3-2.8-6.1-6.1z" fill="#fff"/></svg>
    <div class="contact-text" style="top:416px">02 5550 1234</div>

    <svg class="contact-icon" style="top:431px" viewBox="0 0 14 14"><circle cx="7" cy="7" r="7" fill="var(--green)"/><rect x="3.5" y="4.5" width="7" height="5" rx=".6" fill="#fff"/><path d="M3.7 4.8 7 7.3l3.3-2.5" fill="none" stroke="var(--green)" stroke-width=".8"/></svg>
    <div class="contact-text" style="top:447px">info@thebrightpath.com.au</div>

    <svg class="contact-icon" style="top:461px" viewBox="0 0 14 14"><circle cx="7" cy="7" r="7" fill="var(--green)"/><g fill="none" stroke="#fff" stroke-width=".8"><circle cx="7" cy="7" r="3.8"/><ellipse cx="7" cy="7" rx="1.6" ry="3.8"/><path d="M3.2 7h7.6M3.8 5h6.4M3.8 9h6.4"/></g></svg>
    <div class="contact-text" style="top:477px">www.thebrightpath.com.au</div>
  </div>

  <div class="panel panel--cover">
    <div class="brand" style="top:26px">
      <span class="brand-dot" style="width:30px;height:30px;margin-bottom:10px"></span>
      <span class="brand-name" style="font-size:29px">thebrightpath</span>
    </div>

    <div class="cover-photo" role="img" aria-label="Photo of a smiling teacher and young girl drawing together at a desk"></div>

    <svg class="cover-band" viewBox="0 0 239 140" preserveAspectRatio="none">
      <defs><linearGradient id="coverShade" x1="0" y1="0" x2="0" y2="1"><stop offset="0" stop-color="var(--green-light)"/><stop offset="1" stop-color="var(--green-dark)"/></linearGradient></defs>
      <path d="M0 14C70 -2 160 -2 239 6V14C160 8 70 10 0 26Z" fill="var(--grey-curve)"/>
      <path d="M0 26C70 10 160 8 239 14V140H0Z" fill="url(#coverShade)"/>
      <path d="M0 20C70 4 160 2 239 10V14C160 8 70 10 0 26Z" fill="#fff"/>
    </svg>

    <div class="cover-title" style="top:394px">UNDERSTANDING<br>IDENTIFYING GUIDING</div>
    <div class="pill">www.thebrightpath.com.au</div>
  </div>
</section>

<section class="sheet sheet--inside">

  <div class="panel panel--who">
    <div class="who-photo" role="img" aria-label="Photo of a teacher reading with a young boy who is writing at a table"></div>

    <h2 class="section-title">WHO WE ARE</h2>
    <div class="body-copy body-copy--who" style="top:44px">
      <p>Thebrightpath is a team with a passion for helping people to thrive. We are a team of psychologists and teachers who have experience in both educational and clinical settings.</p>
      <p>We understand the challenges parents face in wanting what is best for their children, trying to understand how and where to access the most relevant information and support.</p>
    </div>

    <svg class="wave" width="239" height="125" viewBox="0 0 239 125" preserveAspectRatio="none">
      <defs><linearGradient id="whoShade" x1="0" y1="0" x2="0" y2="1"><stop offset="0" stop-color="var(--green-light)"/><stop offset="1" stop-color="var(--green-dark)"/></linearGradient></defs>
      <path d="M0 10C70 -4 160 -2 239 10V17C160 6 70 4 0 18Z" fill="var(--grey-curve)"/>
      <path d="M0 18C70 4 160 6 239 17V22C160 12 70 10 0 24Z" fill="#fff"/>
      <path d="M0 24C70 10 160 12 239 22V125H0Z" fill="url(#whoShade)"/>
    </svg>

    <div class="brand brand--light" style="top:408px">
      <span class="brand-dot" style="width:26px;height:26px;margin-bottom:10px"></span>
      <span class="brand-name" style="font-size:28px">thebrightpath</span>
    </div>
  </div>

  <div class="panel panel--about">
    <div class="body-copy" style="top:27px">
      <p>We are passionate about wanting to help families navigate the diagnostic and assessment process.</p>
      <p>We believe that quality and comprehensive assessment needs to happen before intervention begins. We work collaboratively with other professionals to ensure that recommendations and supports put in place are appropriate and evidence-based while also meeting the needs of the individual.</p>
      <p>We are qualified to give formal diagnoses for mental health conditions and specific learning disorders.</p>
    </div>

    <h3 class="includes-title">This includes:</h3>
    <ul class="conditions">
      <li><svg width="7" height="7" viewBox="0 0 8 8"><circle cx="4" cy="4" r="4" fill="var(--green)"/><path d="M2.2 4.1l1.2 1.1 2.4-2.4" fill="none" stroke="#fff" stroke-width="1"/></svg>Attention Deficit Hyperactivity Disorder</li>
      <li><svg width="7" height="7" viewBox="0 0 8 8"><circle cx="4" cy="4" r="4" fill="var(--green)"/><path d="M2.2 4.1l1.2 1.1 2.4-2.4" fill="none" stroke="#fff" stroke-width="1"/></svg>Autism Spectrum Disorder</li>
      <li><svg width="7" height="7" viewBox="0 0 8 8"><circle cx="4" cy="4" r="4" fill="var(--green)"/><path d="M2.2 4.1l1.2 1.1 2.4-2.4" fill="none" stroke="#fff" stroke-width="1"/></svg>Specific Learning Disorders</li>
      <li><svg width="7" height="7" viewBox="0 0 8 8"><circle cx="4" cy="4" r="4" fill="var(--green)"/><path d="M2.2 4.1l1.2 1.1 2.4-2.4" fill="none" stroke="#fff" stroke-width="1"/></svg>Language disorders</li>
      <li><svg width="7" height="7" viewBox="0 0 8 8"><circle cx="4" cy="4" r="4" fill="var(--green)"/><path d="M2.2 4.1l1.2 1.1 2.4-2.4" fill="none" stroke="#fff" stroke-width="1"/></svg>Anxiety Disorders</li>
      <li><svg width="7" height="7" viewBox="0 0 8 8"><circle cx="4" cy="4" r="4" fill="var(--green)"/><path d="M2.2 4.1l1.2 1.1 2.4-2.4" fill="none" stroke="#fff" stroke-width="1"/></svg>Mood Disorders</li>
      <li><svg width="7" height="7" viewBox="0 0 8 8"><circle cx="4" cy="4" r="4" fill="var(--green)"/><path d="M2.2 4.1l1.2 1.1 2.4-2.4" fill="none" stroke="#fff" stroke-width="1"/></svg>Communication Disorders</li>
    </ul>

    <div class="body-copy" style="top:422px">
      <p>We are passionate about collaborating with your school or workplace, supporting you in applying for financial support if available (such as NDIS funding), and to feel more informed and confident in your decisions.</p>
    </div>
  </div>

  <div class="panel panel--process">
    <h2 class="section-title">The process</h2>

    <div class="step" style="top:53px;height:45px"><span class="step-num">1</span><p>An initital face-to-face interview to discuss your concerns and understand the relevant history and details.</p></div>
    <svg class="step-arrow" style="top:103px" width="26" height="22" viewBox="0 0 26 22" fill="var(--green)"><rect x="7" y="0" width="12" height="2"/><rect x="7" y="3.3" width="12" height="2"/><rect x="7" y="6.6" width="12" height="2"/><path d="M0 10h26L13 22z"/></svg>

    <div class="step" style="top:127px;height:55px"><span class="step-num">2</span><p>A formal assessment sessions during which relevant tests are completed. This can include IQ testing, Acehivement testing, Memory testing, Personality profiling etc.</p></div>
    <svg class="step-arrow" style="top:186px" width="26" height="22" viewBox="0 0 26 22" fill="var(--green)"><rect x="7" y="0" width="12" height="2"/><rect x="7" y="3.3" width="12" height="2"/><rect x="7" y="6.6" width="12" height="2"/><path d="M0 10h26L13 22z"/></svg>

    <div class="step" style="top:211px;height:55px"><span class="step-num">3</span><p>obtaining additional informaiton through questionnaires, observation, contact with other professionals (such as teachers/tutors etc).</p></div>
    <svg class="step-arrow" style="top:269px" width="26" height="22" viewBox="0 0 26 22" fill="var(--green)"><rect x="7" y="0" width="12" height="2"/><rect x="7" y="3.3" width="12" height="2"/><rect x="7" y="6.6" width="12" height="2"/><path d="M0 10h26L13 22z"/></svg>

    <div class="step" style="top:294px;height:55px"><span class="step-num">4</span><p>A feedback session during which we provide you with a final draft of the report &amp; discuss possible recommendations, collaborating about the next steps.</p></div>
    <svg class="step-arrow" style="top:352px" width="26" height="22" viewBox="0 0 26 22" fill="var(--green)"><rect x="7" y="0" width="12" height="2"/><rect x="7" y="3.3" width="12" height="2"/><rect x="7" y="6.6" width="12" height="2"/><path d="M0 10h26L13 22z"/></svg>

    <div class="step" style="top:377px;height:57px"><span class="step-num">5</span><p>A copy of the finalised report is provided and opportunity for discussion and engagement with teachers or other allied health is provied.</p></div>

    <svg class="wave" width="239" height="62" viewBox="0 0 239 62" preserveAspectRatio="none">
      <path d="M0 26C80 24 170 14 239 0V6C170 20 80 30 0 32Z" fill="var(--grey-curve)"/>
      <path d="M0 34C80 32 170 22 239 10V62H0Z" fill="var(--green)"/>
    </svg>
    <div class="web-line" style="top:482px">www.thebrightpath.com.au</div>
  </div>
</section>

</body>
</html>
```